Hi, Looking for an upgraded business card to the aged one attached. Open to suggestions and no real limitations, but if your going to use a picture of a taxi i think it should be vector based rather than a full color picture. I've uploaded a 2 pictures of the type of taxi which is a Torvane K5 in white. The taxi markings look like the pink one in the picture but to be clear his is white. The taxi is in Bermuda so if you wanted to include something island based that's ok as well but not required. The other thing he wanted to keep on there was the bermuda police crest, with the retired police office incorporated somehow.

Requirements
Must have
• Bermuda Taxi Operator
Retired Police Officer
Police Crest
Taxi #
Email
Mobile Number

```html
<!DOCTYPE html>
<html lang="en">
<head>
<meta charset="utf-8">
<title>Bermuda Taxi Operator – Business Card</title>
<link rel="stylesheet" href="https://fonts.googleapis.com/css2?family=Raleway:wght@400;700;800&family=Lato:wght@400&display=swap">
<style>
  :root {
    --backdrop: #4a4a4a;
    --card: #ffffff;
    --navy: #0c4a8a;
    --ink: #333333;
    --charcoal: #3d3d3d;
    --van-light: #f1f1f1;
    --van-dark: #b9b9b9;
  }
  * { margin: 0; padding: 0; box-sizing: border-box; }
  html, body { width: 751px; height: 1200px; overflow: hidden; background: var(--backdrop); }
  .canvas { position: relative; width: 751px; height: 1200px; }

  .card { position: absolute; left: 132px; width: 488px; background: var(--card); overflow: hidden; }
  .card-front { top: 283px; height: 297px; }
  .card-back { top: 630px; height: 287px; }

  .emblem { position: absolute; display: flex; flex-direction: column; align-items: center; gap: 6px;
            font-family: "Raleway", sans-serif; font-weight: 700; color: var(--navy); text-align: center;
            letter-spacing: 0.5px; line-height: 1.15; }
  .emblem-dot { width: 22px; height: 22px; border-radius: 50%; background: var(--navy); }
  .card-front .emblem { left: 36px; top: 58px; width: 102px; font-size: 11px; }
  .card-back .emblem { left: 174px; top: 98px; width: 140px; font-size: 15px; gap: 8px; }
  .card-back .emblem-dot { width: 30px; height: 30px; }

  .title { position: absolute; right: 25px; top: 38px; text-align: right;
           font-family: "Raleway", sans-serif; font-weight: 800; font-size: 25.5px; line-height: 32px;
           color: var(--navy); letter-spacing: 0.2px; }
  .holder { position: absolute; right: 25px; top: 124px; text-align: right; font-family: "Raleway", sans-serif; }
  .holder-name { font-weight: 700; font-size: 16px; color: var(--ink); line-height: 19px; }
  .holder-role { font-weight: 400; font-size: 13.5px; color: var(--ink); line-height: 17px; }
  .holder-rule { display: block; margin: 6px 0 0 auto; width: 47px; height: 1.5px; background: var(--navy); }

  .contacts { position: absolute; right: 25px; top: 198px; list-style: none;
              font-family: "Lato", sans-serif; font-size: 11px; color: var(--ink); }
  .contacts li { display: flex; justify-content: flex-end; align-items: center; gap: 10px; height: 14px; margin-bottom: 10.5px; }
  .contacts svg { width: 14px; height: 14px; flex: none; }

  .vehicle { position: absolute; left: 24px; top: 154px; width: 232px; height: 106px; border-radius: 30px 40px 10px 10px;
             background: linear-gradient(180deg, var(--van-light) 0%, #dcdcdc 70%, var(--van-dark) 100%); }

  .base-band { position: absolute; left: 0; bottom: 0; width: 488px; height: 19px; }
  .side-tab { position: absolute; top: 69px; width: 16px; height: 146px; }
  .side-tab.left { left: 0; }
  .side-tab.right { right: 0; }
</style>
</head>
<body>
<main class="canvas">

  <section class="card card-front" aria-label="Card front">
    <div class="emblem"><span class="emblem-dot"></span>HARBOUR CONSTABULARY</div>

    <h1 class="title">BERMUDA<br>TAXI OPERATOR</h1>

    <div class="holder">
      <p class="holder-name">DORIAN KESWICK</p>
      <p class="holder-role">Retired Police Officer</p>
      <span class="holder-rule"></span>
    </div>

    <ul class="contacts">
      <li>Taxi # T2714
        <svg viewBox="0 0 14 14"><rect width="14" height="14" rx="2" fill="var(--charcoal)"/><path d="M3.5 9V6.5L4.6 4h4.8l1.1 2.5V9z" fill="#fff"/><rect x="4" y="9" width="1.5" height="1.5" fill="#fff"/><rect x="8.5" y="9" width="1.5" height="1.5" fill="#fff"/><rect x="5" y="5" width="4" height="1.4" fill="var(--charcoal)"/></svg>
      </li>
      <li>1-441-555-0142
        <svg viewBox="0 0 14 14"><rect width="14" height="14" rx="2" fill="var(--navy)"/><path d="M4.2 3.2l1.6-.2.8 2-1 .9c.5 1.1 1.3 1.9 2.4 2.4l.9-1 2 .8-.2 1.6c-3.6.2-6.7-2.9-6.5-6.5z" fill="#fff"/></svg>
      </li>
      <li>dkeswick@mailbox.example
        <svg viewBox="0 0 14 14"><rect width="14" height="14" rx="2" fill="var(--navy)"/><rect x="2.8" y="4" width="8.4" height="6" fill="none" stroke="#fff" stroke-width="1"/><path d="M2.8 4L7 7.5 11.2 4" fill="none" stroke="#fff" stroke-width="1"/></svg>
      </li>
    </ul>

    <div class="vehicle" role="img" aria-label="Photo of a white Torvane K5 passenger van"></div>

    <svg class="base-band" viewBox="0 0 488 19" preserveAspectRatio="none" aria-hidden="true">
      <polygon points="0,0 254,0 235,19 0,19" fill="var(--charcoal)"/>
      <polygon points="264,0 488,0 488,19 245,19" fill="var(--navy)"/>
    </svg>
  </section>

  <section class="card card-back" aria-label="Card back">
    <svg class="side-tab left" viewBox="0 0 16 146" aria-hidden="true"><polygon points="0,0 16,9 16,137 0,146" fill="var(--navy)"/></svg>
    <div class="emblem"><span class="emblem-dot"></span>HARBOUR CONSTABULARY</div>
    <svg class="side-tab right" viewBox="0 0 16 146" aria-hidden="true"><polygon points="16,0 0,9 0,137 16,146" fill="var(--navy)"/></svg>
  </section>

</main>
</body>
</html>
```